Stationery Design for Consulting Company
Orvel Partners
Creative Brief
Professional
Tomas Wenholt
Director
Orvel Partners LLC 48215 Ridgefern Road Dunmore, DE 19872 USA
tomas@orvel-advisory.com
www.orvel-advisory.com
Maybe just a larger logo in the middle unless you have better ideas. I'm open to suggestions.

```html
<!DOCTYPE html>
<html lang="en">
<head>
<meta charset="utf-8">
<title>Orvel Partners – Business Card</title>
<link rel="stylesheet" href="https://fonts.googleapis.com/css2?family=Open+Sans:wght@400;600;700&display=swap">
<style>
  :root {
    --bg: #e9e7e4;
    --card-dark: #2b2b2d;
    --band-dark: #3a3a3c;
    --accent: #f2a91a;
    --paper: #ffffff;
    --ink: #2e2e30;
    --ink-soft: #6a6a6d;
  }
  html, body {
    margin: 0;
    padding: 0;
    overflow: hidden;
  }
  .canvas {
    position: relative;
    width: 1200px;
    height: 912px;
    background: var(--bg);
    overflow: hidden;
    font-family: "Open Sans", Arial, sans-serif;
  }
  .card {
    position: absolute;
    width: 560px;
    height: 320px;
    border-radius: 18px;
    overflow: hidden;
    box-shadow: 0 10px 28px rgba(0,0,0,0.18);
  }
  /* Front */
  .card-front {
    left: 90px;
    top: 110px;
    background: var(--card-dark);
    display: flex;
    align-items: center;
    justify-content: center;
  }
  .brand {
    display: flex;
    flex-direction: column;
    align-items: center;
    gap: 10px;
  }
  .brand-row {
    display: flex;
    align-items: center;
    gap: 14px;
  }
  .brand-mark {
    width: 22px;
    height: 22px;
    background: var(--accent);
  }
  .brand-name {
    font-weight: 700;
    color: var(--accent);
    font-size: 38px;
    letter-spacing: 1px;
    line-height: 1;
  }
  .brand-tagline {
    font-size: 10px;
    letter-spacing: 3px;
    text-transform: uppercase;
    color: #cfcfcf;
  }
  /* Back */
  .card-back {
    left: 560px;
    top: 470px;
    background: var(--paper);
  }
  .card-back .sweep {
    position: absolute;
    inset: 0;
  }
  .brand-back {
    position: absolute;
    right: 30px;
    top: 40px;
    align-items: flex-end;
    gap: 8px;
  }
  .brand-back .brand-name {
    font-size: 24px;
  }
  .brand-back .brand-mark {
    width: 14px;
    height: 14px;
  }
  .brand-back .brand-tagline {
    font-size: 7px;
    letter-spacing: 2px;
    color: var(--ink-soft);
  }
  .contact {
    position: absolute;
    left: 30px;
    top: 92px;
    color: var(--ink);
  }
  .contact-name {
    font-weight: 700;
    font-size: 17px;
    margin: 0;
  }
  .contact-role {
    font-size: 12px;
    color: var(--ink-soft);
    margin: 2px 0 12px;
  }
  .contact-list {
    list-style: none;
    margin: 0;
    padding: 0;
    font-size: 10.5px;
    line-height: 1.55;
  }
  .contact-list li {
    display: flex;
    align-items: flex-start;
    gap: 7px;
  }
  .contact-list svg {
    width: 10px;
    height: 10px;
    margin-top: 3px;
    flex: none;
  }
</style>
</head>
<body>
<div class="canvas">

  <section class="card card-front" aria-label="Business card front">
    <div class="brand">
      <div class="brand-row">
        <span class="brand-mark"></span>
        <span class="brand-name">ORVEL PARTNERS LLC</span>
      </div>
      <span class="brand-tagline">Strategy Advisory &amp; Management</span>
    </div>
  </section>

  <section class="card card-back" aria-label="Business card back">
    <svg class="sweep" viewBox="0 0 560 320" width="560" height="320" aria-hidden="true">
      <path d="M0,258 C200,272 400,212 560,100 L560,320 L0,320 Z" fill="var(--band-dark)"/>
      <path d="M0,246 C200,260 392,200 560,86" fill="none" stroke="var(--accent)" stroke-width="5"/>
    </svg>

    <div class="brand brand-back">
      <div class="brand-row">
        <span class="brand-mark"></span>
        <span class="brand-name">ORVEL PARTNERS LLC</span>
      </div>
      <span class="brand-tagline">Strategy Advisory &amp; Management</span>
    </div>

    <div class="contact">
      <p class="contact-name">Tomas Wenholt</p>
      <p class="contact-role">Director</p>
      <ul class="contact-list">
        <li>
          <svg viewBox="0 0 10 10"><path d="M5 0.5a3.2 3.2 0 0 0-3.2 3.2C1.8 6 5 9.5 5 9.5S8.2 6 8.2 3.7A3.2 3.2 0 0 0 5 0.5zm0 4.4a1.2 1.2 0 1 1 0-2.4 1.2 1.2 0 0 1 0 2.4z" fill="var(--ink)"/></svg>
          <span>48215 Ridgefern Road<br>Dunmore, DE 19872 USA</span>
        </li>
        <li>
          <svg viewBox="0 0 10 10"><path d="M2.2 0.8l1.6 2-1 1.2c.6 1.3 1.6 2.3 2.9 2.9l1.2-1 2 1.6-.9 1.7C5 8.9 1.1 5 0.5 1.7z" fill="var(--ink)"/></svg>
          <span>302 555 0148</span>
        </li>
        <li>
          <svg viewBox="0 0 10 10"><rect x="0.5" y="2" width="9" height="6" fill="none" stroke="var(--ink)" stroke-width="1"/><path d="M0.5 2L5 5.5 9.5 2" fill="none" stroke="var(--ink)" stroke-width="1"/></svg>
          <span>tomas@orvel-advisory.com</span>
        </li>
        <li>
          <svg viewBox="0 0 10 10"><circle cx="5" cy="5" r="4.3" fill="none" stroke="var(--ink)" stroke-width="1"/><path d="M0.7 5h8.6M5 0.7c-2 2.4-2 6.2 0 8.6M5 0.7c2 2.4 2 6.2 0 8.6" fill="none" stroke="var(--ink)" stroke-width="0.8"/></svg>
          <span>www.orvel-advisory.com</span>
        </li>
      </ul>
    </div>
  </section>

</div>
</body>
</html>
```